'Halbrook Video' - Website Template Design (that I can use in Word Press)

I would like a professional, colorful website template (4 pages) designed in a format that can be used with Word Press. Upon completion of the design, I would like to take over and maintain/host using Web Press and my Net Parrot account.

My business is videography - producing videos for companies, organizations and not-for-profit charities. Our company will do everything, including writing, planning, producing, directing filming and editing videos etc.

I have a colorful logo and business card already designed and I would like the website built around the look of the logo and business card.

I would like an index page designed first. Once the designer has created an index page I like best, I would like three more pages created with that same design.

1) A 'contact us' page
2) A page with a plug in that would allow me to upload video or connect to ClipVane to show samples of my videography
3) A general template page I could add new pages to in the future.

Target Market(s)

businesses of all kinds, organizations, governments, not-for-profit charities

Industry/Entity Type

Film Production

Number of Pages Required

4 page

Font styles to use
Sans Serif

Requirements
Must have
• 1) Index page
• 2) Contact Us page
• 2) A page with a plug in that would allow me to upload video or connect to ClipVane to show samples of my videography
• 3) A general template page I could add new pages to in the future
Nice to have
• Surprise me! I love lots of color and am open to creative ideas.

```html
<!DOCTYPE html>
<html lang="en">
<head>
<meta charset="utf-8">
<title>Halbrook Video</title>
<link href="https://fonts.googleapis.com/css2?family=Raleway:wght@500;700;800&family=Open+Sans:ital,wght@0,400;0,600;1,400&display=swap" rel="stylesheet">
<style>
:root{
  --orange:#f0582a;--green:#8dc63f;--purple:#6b2a8c;--yellow:#f2e200;--navy:#24338a;--red:#e2262d;
  --ink:#222;--grey:#666;--light:#f2f2f2;--dark:#121212;--white:#fff;
}
*{margin:0;padding:0;box-sizing:border-box}
html,body{width:1200px;height:4027px;overflow:hidden}
body{position:relative;font-family:"Open Sans",Arial,sans-serif;color:var(--ink);background:var(--white)}
.abs{position:absolute}
h2,h3,.nav a,.brand{font-family:"Raleway",Arial,sans-serif}
.center{text-align:center;left:0;width:1200px}

/* header */
.topline{top:0;left:0;width:1200px;height:5px;background:var(--orange)}
.nav{top:0;left:0;width:1200px;height:89px;background:var(--white)}
.nav a{position:absolute;top:38px;font-size:13px;font-weight:700;color:var(--ink);text-decoration:none;text-transform:uppercase;white-space:nowrap}
.nav a.active{color:var(--orange)}
.badge{top:0;left:510px;width:180px;height:200px;z-index:3}
.badge .brand{position:absolute;top:100px;left:0;width:180px;text-align:center;font-size:22px;font-weight:800;color:var(--ink);line-height:1.1;text-transform:uppercase;letter-spacing:1px}

/* hero */
.hero{top:89px;left:0;width:1200px;height:510px;background:linear-gradient(120deg,#3a3532,#1e1c1b 45%,#4a4440);clip-path:polygon(0 0,100% 0,100% 470px,600px 510px,0 470px)}
.hero-title{top:390px;font-size:60px;font-weight:800;color:var(--white);letter-spacing:2px}
.hero-sub{top:478px;font-size:20px;font-weight:700;color:var(--white);letter-spacing:12px}
.hero-line{top:492px;height:2px;width:80px;background:var(--white)}
.dot{top:556px;width:11px;height:11px;border-radius:50%;background:var(--white)}

/* shared headings */
.mark{width:28px;height:28px;left:586px}
.sec-title{font-size:25px;font-weight:800;text-transform:uppercase}
.sec-sub{font-size:11px;font-style:italic;color:var(--grey)}

/* services */
.deco{background:#fbe7ea;opacity:.7}
.svc{width:300px;text-align:center}
.svc .disc{margin:0 auto;width:160px;height:160px;border-radius:50%;display:flex;align-items:center;justify-content:center}
.svc .core{width:134px;height:134px;border-radius:50%;display:flex;align-items:center;justify-content:center}
.svc h3{margin-top:28px;font-size:18px;font-weight:800;text-transform:uppercase}
.svc .rule{margin:8px auto 14px;width:52px;height:3px}
.svc p{font-size:11.5px;line-height:1.65;color:#333;width:250px;margin:0 auto}

/* about */
.about{top:1482px;left:0;width:1200px;height:462px;background:var(--green)}
.about h2{color:var(--white);font-size:26px;font-weight:800;line-height:1.15;text-transform:uppercase}
.about .lead{color:var(--white);font-size:15.5px;line-height:1.42}
.about .body{color:var(--white);font-size:10.5px;line-height:1.55;opacity:.95}
.video{left:588px;top:83px;width:451px;height:298px;background:linear-gradient(135deg,#2d3a4a,#5a6c7e 50%,#1d2530)}

/* featured */
.work{top:2110px;width:212px;height:226px}
.cap{top:2352px;width:212px;text-align:center}
.cap h3{font-size:14px;font-weight:800;text-transform:uppercase}
.cap p{margin-top:6px;font-size:10.5px;line-height:1.55;color:#444}
.arrow{top:2445px;width:26px;height:26px;border-radius:50%;background:#d4d4d4}

/* testimonials */
.testi{top:2502px;left:0;width:1200px;height:371px;background:var(--orange)}
.testi .sec-title{color:var(--white)}
.avatar{left:164px;top:143px;width:144px;height:144px;border-radius:50%;border:5px solid var(--white);background:linear-gradient(135deg,#d9c8b8,#8f7c6d)}
.quote{left:322px;top:148px;width:717px;font-size:12.5px;line-height:1.9;font-style:italic;color:var(--white)}
.qmark{font-family:Georgia,serif;font-size:34px;font-style:normal;line-height:0;vertical-align:-10px}
.who{left:322px;top:291px;font-size:12.5px;font-weight:700;color:var(--white)}

/* what we do */
.wwd{top:2873px;left:0;width:1200px;height:607px;background:var(--light)}
.card{top:164px;width:277px;height:378px;text-align:center;color:var(--white)}
.card .pic{margin:8px;height:207px}
.card h3{margin-top:24px;font-size:14px;font-weight:700;text-transform:uppercase}
.card p{margin:10px auto 0;width:220px;font-size:10.5px;line-height:1.55}
.card .more{display:block;margin-top:14px;font-family:"Raleway",Arial,sans-serif;font-size:12px;font-weight:800}

/* footer */
.footer{top:3480px;left:0;width:1200px;height:547px;background:var(--dark)}
.foot-logo{left:554px;top:-36px;width:92px;height:92px;border-radius:50%;background:var(--white);display:flex;align-items:center;justify-content:center;text-align:center;font-family:"Raleway",Arial,sans-serif;font-size:11px;font-weight:800;color:var(--orange);line-height:1.2;text-transform:uppercase}
.footer .sec-title{color:var(--white)}
.footer .sec-sub{color:#aaa}
.field{left:161px;width:486px;height:38px;background:var(--white);font-size:11px;font-style:italic;color:#555;padding:11px 12px}
.submit{background:var(--orange);color:var(--white);font-family:"Raleway",Arial,sans-serif;font-weight:800;font-size:13px;display:flex;align-items:center;justify-content:center}
.col-head{font-family:"Raleway",Arial,sans-serif;color:var(--white);font-size:16px;font-weight:800;text-transform:uppercase}
.addr{left:698px;top:190px;width:330px;font-size:11.5px;line-height:1.6;color:#ccc}
.line{left:698px;font-size:11px;color:#ccc;display:flex;gap:10px;width:330px}
.line svg{flex:none;margin-top:2px}
.social{top:494px;width:24px;height:24px;border-radius:50%;border:2px solid var(--white)}
.copy{left:693px;top:496px;font-size:10px;color:#bbb}
.copy span{color:var(--white)}
</style>
</head>
<body>

<div class="abs topline"></div>
<nav class="abs nav">
  <a class="active" style="left:166px">Home</a>
  <a style="left:255px">Video Production</a>
  <a style="left:424px">About</a>
  <a style="left:700px">Our Services</a>
  <a style="left:835px">Projects</a>
  <a style="left:948px">Contact Us</a>
</nav>
<div class="abs badge">
  <svg width="180" height="200" viewBox="0 0 180 200"><polygon points="0,0 180,0 180,160 90,200 0,160" fill="#fff"/></svg>
  <div class="brand">Halbrook<br>Video</div>
</div>

<section class="abs hero" role="img" aria-label="Dark photograph of vintage film reels and movie equipment"></section>
<div class="abs center hero-title brand">HALBROOK</div>
<div class="abs hero-line" style="left:430px"></div>
<div class="abs center hero-sub brand">VIDEO</div>
<div class="abs hero-line" style="left:690px"></div>
<div class="abs dot" style="left:573px"></div>
<div class="abs dot" style="left:588px"></div>
<div class="abs dot" style="left:603px;background:var(--orange)"></div>
<div class="abs dot" style="left:618px"></div>

<!-- services -->
<div class="abs deco" style="left:118px;top:840px;width:46px;height:40px"></div>
<div class="abs deco" style="left:76px;top:970px;width:44px;height:36px"></div>
<div class="abs deco" style="left:460px;top:930px;width:60px;height:56px;background:#f3f0cf"></div>
<div class="abs deco" style="left:660px;top:870px;width:60px;height:80px;background:#e6e8f4"></div>
<div class="abs deco" style="left:1042px;top:830px;width:46px;height:40px;background:#e3f1d4"></div>
<div class="abs deco" style="left:1070px;top:950px;width:44px;height:36px"></div>

<div class="abs mark" style="top:662px;background:var(--orange)"></div>
<h2 class="abs center sec-title" style="top:718px">Video Production Services</h2>
<div class="abs center sec-sub" style="top:757px">Sed ut perspiciatis unde omnis iste natus error sit voluptatem accusantium doloremque laudantium, totam</div>

<div class="abs svc" style="left:153px;top:800px">
  <div class="disc" style="background:#f6a489"><div class="core" style="background:var(--orange)">
    <svg width="60" height="60" viewBox="0 0 60 60"><path d="M12 48 L44 16 L50 22 L18 54 Z" fill="#fff"/><path d="M12 48 L8 58 L18 54 Z" fill="#fff"/></svg>
  </div></div>
  <h3 style="color:var(--orange)">Writing</h3><div class="rule" style="background:var(--orange)"></div>
  <p>Lorem ipsum dolor sit amet, conetur adip iscing elit, sed do eiusmod tempor incididunt laboeet dolore magna aliquac enim ad</p>
</div>
<div class="abs svc" style="left:449px;top:800px">
  <div class="disc" style="background:#c6e29f"><div class="core" style="background:var(--green)">
    <svg width="60" height="60" viewBox="0 0 60 60"><rect x="12" y="8" width="34" height="44" rx="3" fill="#fff"/><rect x="18" y="18" width="22" height="3" fill="#8dc63f"/><rect x="18" y="26" width="22" height="3" fill="#8dc63f"/><rect x="18" y="34" width="14" height="3" fill="#8dc63f"/></svg>
  </div></div>
  <h3 style="color:var(--green)">Planning</h3><div class="rule" style="background:var(--green)"></div>
  <p>Lorem ipsum dolor sit amet, conetur adip iscing elit, sed do eiusmod tempor incididunt laboeet dolore magna aliquac enim ad</p>
</div>
<div class="abs svc" style="left:747px;top:800px">
  <div class="disc" style="background:#b595c6"><div class="core" style="background:var(--purple)">
    <svg width="60" height="60" viewBox="0 0 60 60"><circle cx="20" cy="18" r="7" fill="#fff"/><circle cx="36" cy="18" r="7" fill="#fff"/><rect x="10" y="28" width="30" height="20" rx="3" fill="#fff"/><polygon points="40,38 52,30 52,46" fill="#fff"/></svg>
  </div></div>
  <h3 style="color:var(--purple)">Producing</h3><div class="rule" style="background:var(--purple)"></div>
  <p>Lorem ipsum dolor sit amet, conetur adip iscing elit, sed do eiusmod tempor incididunt laboeet dolore magna aliquac enim ad</p>
</div>

<div class="abs svc" style="left:153px;top:1123px">
  <div class="disc" style="background:#f8f08c"><div class="core" style="background:var(--yellow)">
    <svg width="60" height="60" viewBox="0 0 60 60"><path d="M14 6 H38 L48 16 V54 H14 Z" fill="#fff"/><polygon points="25,22 39,31 25,40" fill="#f2e200"/></svg>
  </div></div>
  <h3 style="color:var(--yellow)">Editing Videos</h3><div class="rule" style="background:var(--yellow)"></div>
  <p>Lorem ipsum dolor sit amet, conetur adip iscing elit, sed do eiusmod tempor incididunt laboeet dolore magna aliquac enim ad</p>
</div>
<div class="abs svc" style="left:449px;top:1123px">
  <div class="disc" style="background:#8e97c4"><div class="core" style="background:var(--navy)">
    <svg width="60" height="60" viewBox="0 0 60 60"><circle cx="20" cy="18" r="7" fill="#fff"/><circle cx="36" cy="18" r="7" fill="#fff"/><rect x="10" y="28" width="30" height="20" rx="3" fill="#fff"/><polygon points="40,38 52,30 52,46" fill="#fff"/></svg>
  </div></div>
  <h3 style="color:var(--navy)">Directing Filming</h3><div class="rule" style="background:var(--navy)"></div>
  <p>Lorem ipsum dolor sit amet, conetur adip iscing elit, sed do eiusmod tempor incididunt laboeet dolore magna aliquac enim ad</p>
</div>
<div class="abs svc" style="left:747px;top:1123px">
  <div class="disc" style="background:#f09296"><div class="core" style="background:var(--red)">
    <svg width="60" height="60" viewBox="0 0 60 60"><circle cx="30" cy="30" r="20" fill="#fff"/><circle cx="30" cy="20" r="4" fill="#e2262d"/><circle cx="30" cy="40" r="4" fill="#e2262d"/><circle cx="20" cy="30" r="4" fill="#e2262d"/><circle cx="40" cy="30" r="4" fill="#e2262d"/></svg>
  </div></div>
  <h3 style="color:var(--red)">Other Services</h3><div class="rule" style="background:var(--red)"></div>
  <p>Lorem ipsum dolor sit amet, conetur adip iscing elit, sed do eiusmod tempor incididunt laboeet dolore magna aliquac enim ad</p>
</div>

<!-- about -->
<section class="abs about">
  <div class="abs" style="left:161px;top:90px;width:46px;height:46px;background:var(--white)"></div>
  <h2 class="abs" style="left:222px;top:90px;width:340px">About Video<br>Production Company</h2>
  <p class="abs lead" style="left:161px;top:162px;width:380px">Sed ut perspiciatis unde omnis iste natus error sit voluptatem accusantium doloremque laudantium, totam rem aperiam, eaque ipsa qua.</p>
  <p class="abs body" style="left:161px;top:250px;width:400px">Sed ut perspiciatis unde omnis iste natus error sit voluptatem accusantium doloremque laudantium, totam rem aperiam, eaque ipsa quae ab illo inventore veritatis et quasi architecto beatae vitae dicta sunt explicabo. Nemo enim ipsam voluptatem quia voluptas sit aspernatur aut odit aut fugit, sed quia consequuntur magni dolores eos qui ratione voluptatem sequi nesciunt. Neque porro quisquam est, qui dolorem ipsum quia dolor sit amet, consectetur, adipisci velit, sed quia non numquam eius modi tempora incidunt ut labore et dolore magnam aliquam quaerat voluptatem.</p>
  <div class="abs video" role="img" aria-label="Video still of an editor working at a studio mixing desk with monitors"></div>
  <svg class="abs" style="left:763px;top:181px" width="102" height="102" viewBox="0 0 102 102"><circle cx="51" cy="51" r="46" fill="rgba(255,255,255,.25)" stroke="#fff" stroke-width="5"/><polygon points="40,30 72,51 40,72" fill="#fff"/></svg>
</section>

<!-- featured -->
<div class="abs deco" style="left:118px;top:2160px;width:46px;height:40px;background:#ece8f4"></div>
<div class="abs deco" style="left:76px;top:2298px;width:44px;height:36px"></div>
<div class="abs deco" style="left:1044px;top:2160px;width:46px;height:40px;background:#fde8dc"></div>
<div class="abs mark" style="top:1976px;background:var(--purple)"></div>
<h2 class="abs center sec-title" style="top:2034px">Featured Work</h2>
<div class="abs center sec-sub" style="top:2070px">Sed ut perspiciatis unde omnis iste natus error sit voluptatem accusantium doloremque laudantium, totam</div>

<div class="abs work" style="left:161px;background:linear-gradient(160deg,#6b7a86,#2c3036 70%)" role="img" aria-label="Film set with clapperboard and studio lights"></div>
<div class="abs work" style="left:384px;background:linear-gradient(160deg,#9aa86a,#c9e04a 50%,#5a5a3c)" role="img" aria-label="Fashion shoot with a model in a bright yellow dress"></div>
<div class="abs work" style="left:607px;background:linear-gradient(160deg,#e8c9c4,#b44a5a 55%,#3a2a2a)" role="img" aria-label="Wedding celebration scene in warm tones"></div>
<div class="abs work" style="left:830px;background:linear-gradient(160deg,#2a2a3a,#b3222a 55%,#1a1a22)" role="img" aria-label="Portrait shoot of a model in a red gown on a dark set"></div>

<div class="abs cap" style="left:161px"><h3>Sed ut perspiciati</h3><p>Sed ut perspiciatis unde omnis iste natus error sit voluptatem accusantium</p></div>
<div class="abs cap" style="left:384px"><h3>Sed ut perspiciati</h3><p>Sed ut perspiciatis unde omnis iste natus error sit voluptatem accusantium</p></div>
<div class="abs cap" style="left:607px"><h3>Sed ut perspiciati</h3><p>Sed ut perspiciatis unde omnis iste natus error sit voluptatem accusantium</p></div>
<div class="abs cap" style="left:830px"><h3>Sed ut perspiciati</h3><p>Sed ut perspiciatis unde omnis iste natus error sit voluptatem accusantium</p></div>

<svg class="abs arrow" style="left:565px" viewBox="0 0 26 26"><path d="M15 8 L10 13 L15 18" stroke="#fff" stroke-width="2.5" fill="none"/></svg>
<svg class="abs arrow" style="left:604px" viewBox="0 0 26 26"><path d="M11 8 L16 13 L11 18" stroke="#fff" stroke-width="2.5" fill="none"/></svg>

<!-- testimonials -->
<section class="abs testi">
  <div class="abs mark" style="top:40px;background:var(--white)"></div>
  <h2 class="abs center sec-title" style="top:94px">Testimonials</h2>
  <div class="abs avatar" role="img" aria-label="Round portrait of the client giving the testimonial"></div>
  <p class="abs quote"><span class="qmark">&ldquo;</span> Sed ut perspiciatis unde omnis iste natus error sit voluptatem accusantium doloremque laudantium, totam rem aperiam, eaque ipsa quae ab illo inventore veritatis et quasi architecto beatae vitae dicta sunt explicabo. Nemo enim ipsam voluptatem quia voluptas sit aspernatur aut odit aut fugit, sed quia consequuntur magni dolores eos qui ratione voluptatem sequi nesciunt. Neque porro quisquam est, qui dolorem ipsum quia dolor sit amet, consectetur, adipisci velit, sed quia non numquam eius modi tempora. Ut enim ad minima veniam, nisi ut aliquid ex ea commodi. <span class="qmark">&rdquo;</span></p>
  <div class="abs who">DANA WELLER , CITY NAME</div>
</section>

<!-- what we do -->
<section class="abs wwd">
  <div class="abs mark" style="top:40px;background:var(--green)"></div>
  <h2 class="abs center sec-title" style="top:92px">What We Do</h2>
  <div class="abs center sec-sub" style="top:128px">Sed ut perspiciatis unde omnis iste natus error sit voluptatem accusantium doloremque laudantium, totam</div>
  <div class="abs card" style="left:161px;background:var(--navy)">
    <div class="pic" style="background:linear-gradient(160deg,#c9c2b8,#4a4a4a)" role="img" aria-label="Crew member holding a clapperboard"></div>
    <h3>Companies</h3><p>Sed ut perspiciatis unde omnis iste natus error sit voluptatem accusantiumt at per iciatis unde omnis iste natus sit ec.</p><span class="more">READ MORE</span>
  </div>
  <div class="abs card" style="left:464px;background:var(--green)">
    <div class="pic" style="background:linear-gradient(160deg,#8a8580,#2a2826)" role="img" aria-label="Vintage film camera and reels on a table"></div>
    <h3>Organizations</h3><p>Sed ut perspiciatis unde omnis iste natus error sit voluptatem accusantiumt at per iciatis unde omnis iste natus sit ec.</p><span class="more">READ MORE</span>
  </div>
  <div class="abs card" style="left:768px;background:var(--purple)">
    <div class="pic" style="background:linear-gradient(160deg,#d8c4ae,#6a5a4c)" role="img" aria-label="Volunteers gathered around a laptop"></div>
    <h3>Not-for-profit charities</h3><p>Sed ut perspiciatis unde omnis iste natus error sit voluptatem accusantiumt at per iciatis unde omnis iste natus sit ec.</p><span class="more">READ MORE</span>
  </div>
</section>

<!-- footer / contact -->
<footer class="abs footer">
  <div class="abs foot-logo">Halbrook<br>Video</div>
  <h2 class="abs center sec-title" style="top:88px">Contact Us</h2>
  <div class="abs center sec-sub" style="top:124px">Sed ut perspiciatis unde omnis iste natus error sit voluptatem accusantium doloremque laudantium, totam</div>

  <div class="abs field" style="top:161px">Name:</div>
  <div class="abs field" style="top:212px">Email:</div>
  <div class="abs field" style="top:263px">Phone:</div>
  <div class="abs field" style="top:311px;height:143px">Message:</div>
  <div class="abs submit" style="left:507px;top:406px;width:140px;height:48px">SUBMIT</div>

  <div class="abs col-head" style="left:698px;top:152px">Address</div>
  <p class="abs addr">Sed ut perspiciatis unde omnis iste natusvoluptatem accusantium dolor emque laudantiu ut perspiciatis unde omnis iste natus</p>
  <div class="abs line" style="top:266px"><svg width="10" height="12" viewBox="0 0 10 12"><path d="M5 0 A5 5 0 0 1 10 5 C10 8 5 12 5 12 C5 12 0 8 0 5 A5 5 0 0 1 5 0Z" fill="#ccc"/></svg><span>Ad ut perspiciatis unde omnis iste natus<br>oluptatem accusantium doloremque laudantiu</span></div>
  <div class="abs line" style="top:305px"><svg width="10" height="12" viewBox="0 0 10 12"><rect x="2" y="0" width="6" height="12" rx="1" fill="#ccc"/></svg><span>Tel: 555-014-2290 (OFTC)</span></div>
  <div class="abs line" style="top:326px"><svg width="10" height="12" viewBox="0 0 10 12"><rect x="0" y="3" width="10" height="8" fill="#ccc"/><rect x="2" y="0" width="6" height="3" fill="#ccc"/></svg><span>Fax: 555-014-2291</span></div>
  <div class="abs line" style="top:347px"><svg width="11" height="12" viewBox="0 0 11 12"><rect x="0" y="2" width="11" height="8" fill="#ccc"/><path d="M0 2 L5.5 7 L11 2" stroke="#121212" fill="none"/></svg><span>hello@halbrookvideo.test</span></div>

  <div class="abs col-head" style="left:698px;top:372px">Newsletter</div>
  <div class="abs field" style="left:698px;top:408px;width:242px;height:40px">Email:</div>
  <div class="abs submit" style="left:940px;top:408px;width:99px;height:40px;background:var(--green)">SUBMIT</div>

  <div class="abs social" style="left:161px"></div>
  <div class="abs social" style="left:193px"></div>
  <div class="abs social" style="left:225px"></div>
  <div class="abs social" style="left:257px"></div>
  <div class="abs copy">Copyright &copy; 2016. All Rights Reserved Halbrook &nbsp;<span>Terms and conditions</span></div>
</footer>

</body>
</html>
```